Trifold brochure

Need a trifold marketing brochure for my autism therapy for children business . I would be interested in having designs in both English and Spanish if possible!!!!! Website is www.meadowlarkcareaba.com
Address on brochure needs to be 2718 Tamarind Ave W Suite 5
Minneapolis, MN 55192
Updates
Can you update the address on brochure to 2718 Tamarind Ave W Suite 5
Minneapolis, MN 55192
Target Market(s)
Autism therapy for children
Industry/Entity Type
Autism Therapy
Look and feel
Each slider illustrates characteristics of the customer's brand and the style your logo design should communicate.

```html
<!DOCTYPE html>
<html lang="en">
<head>
<meta charset="utf-8">
<title>Meadowlark Care Behavioral Therapy – Trifold Brochure</title>
<link href="https://fonts.googleapis.com/css2?family=Oswald:wght@500;600&family=Montserrat:wght@400;500;600;700&family=Lora:ital,wght@1,500&display=swap" rel="stylesheet">
<style>
  :root{
    --blue:#1d5b97;
    --blue-deep:#174a7c;
    --gold:#b08a48;
    --gold-light:#c9a262;
    --ink:#24262b;
    --body:#3b3f46;
    --white:#ffffff;
  }
  *{margin:0;padding:0;box-sizing:border-box}
  html,body{width:1200px;height:3498px;overflow:hidden}
  body{background:linear-gradient(180deg,#dcdddf,#c9cacc);font-family:"Montserrat",sans-serif;position:relative}
  .spread-frame{position:absolute;left:20px;width:1160px;height:894px;box-shadow:0 18px 40px rgba(0,0,0,.25)}
  .spread-frame.outside{top:785px}
  .spread-frame.inside{top:1819px}
  .spread{position:absolute;left:0;top:0;width:681px;height:525px;transform:scale(1.70338);transform-origin:0 0;overflow:hidden;background:var(--white)}
  .spread>svg.shapes{position:absolute;left:0;top:0;width:681px;height:525px}
  .abs{position:absolute}

  /* brand name */
  .brand{position:absolute;text-align:center;font-family:"Montserrat",sans-serif;font-weight:600;line-height:1.05;letter-spacing:.02em}
  .brand .dot{display:block;margin:0 auto 5px;border-radius:50%}
  .brand .line2{display:block;font-size:.62em;letter-spacing:.06em}

  /* outside: about panel */
  .tab-title{position:absolute;color:var(--white);font-weight:600;letter-spacing:.02em}
  .about-title{left:45px;top:12px;font-size:10.5px}
  .about-text{left:23px;top:46px;width:192px;font-size:5.6px;line-height:9.6px;color:var(--body)}
  .value{position:absolute;left:23px;width:195px}
  .value h3{display:flex;align-items:center;gap:7px;font-size:9.5px;color:var(--blue);font-weight:700}
  .value h3 svg{width:22px;height:22px}
  .value p{margin-top:6px;font-size:5.6px;line-height:9.6px;color:var(--body)}
  .value.vision{top:121px}
  .value.mission{top:202px}
  .value.motto{top:289px}

  /* outside: contact panel */
  .contact{position:absolute;left:227px;width:227px;text-align:center;color:var(--white)}
  .contact-title{top:319px;font-size:8px;font-weight:600;letter-spacing:.06em}
  .contact-icons{top:343px;display:flex;justify-content:center;gap:6px}
  .contact-icons span{width:17px;height:17px;border:1.3px solid var(--gold-light);border-radius:50%;display:flex;align-items:center;justify-content:center}
  .contact-icons svg{width:9px;height:9px}
  .contact-address{top:373px;font-size:6.6px;line-height:12px;letter-spacing:.02em}
  .contact-phone{top:414px;font-size:13px;font-weight:600;letter-spacing:.03em}
  .contact-email{top:446px;font-size:6.2px}
  .web-pill{position:absolute;left:257px;top:470px;width:169px;height:23px;border-radius:12px;background:var(--gold);color:var(--white);font-size:7px;font-weight:500;display:flex;align-items:center;justify-content:center;border:1.5px solid #d8bb85}

  /* outside: cover panel */
  .cover{position:absolute;left:454px;width:227px;text-align:center}
  .headline{font-family:"Oswald",sans-serif;font-weight:600;line-height:1;text-transform:uppercase}
  .cover-head-1{top:385px;font-size:25px;color:var(--ink)}
  .cover-head-2{top:413px;font-size:25px;color:var(--gold)}
  .cover-tag{top:443px;font-family:"Lora",serif;font-style:italic;font-weight:500;font-size:7.5px;color:var(--ink)}
  .phone-pill{position:absolute;display:flex;align-items:center;justify-content:center;gap:5px;border-radius:13px;color:var(--white);font-weight:600;letter-spacing:.03em}
  .phone-pill svg{width:10px;height:10px}
  .cover-phone{left:482px;top:468px;width:169px;height:25px;background:var(--blue);font-size:14px;border:1.5px solid #5d8dc0}
  .cover-web{top:505px;font-size:7.5px;color:var(--white);font-weight:500}

  /* inside: services */
  .services-title{left:38px;top:8px;font-size:16px;letter-spacing:.03em}
  .card{position:absolute;width:165px;border-radius:0 0 7px 7px;overflow:hidden}
  .card .photo{height:102px}
  .card .label{height:34px;display:flex;align-items:center;justify-content:center;text-align:center;color:var(--white);font-size:6.8px;font-weight:600;line-height:1.3;padding:0 8px}
  .card.gold .label{background:var(--gold)}
  .card.blue .label{background:var(--blue)}
  .card.c1{left:32px}.card.c2{left:258px}
  .card.r1{top:56px}.card.r2{top:211px}

  /* inside: next step */
  .cta{position:absolute;left:454px;width:227px;text-align:center;color:var(--white)}
  .cta-head-1{top:110px;font-size:26px;font-family:"Oswald",sans-serif;font-weight:500;line-height:1}
  .cta-head-2{top:142px;font-size:26px;font-family:"Oswald",sans-serif;font-weight:500;line-height:1}
  .cta-star{top:179px;color:var(--gold-light);font-size:9px}
  .cta-tag{top:199px;font-family:"Lora",serif;font-style:italic;font-weight:500;font-size:9px;line-height:16px}
  .cta-phone{left:479px;top:242px;width:177px;height:25px;background:var(--gold);font-size:14px;border:1.5px solid #d8bb85}
  .cta-web{top:278px;font-size:7.5px;font-weight:500}
</style>
</head>
<body>

<!-- OUTSIDE SPREAD -->
<div class="spread-frame outside">
  <div class="spread">
    <svg class="shapes" viewBox="0 0 681 525">
      <defs>
        <linearGradient id="coverPhoto" x1="0" y1="0" x2="1" y2="1">
          <stop offset="0" stop-color="#c9a46c"/>
          <stop offset=".35" stop-color="#b9663f"/>
          <stop offset=".6" stop-color="#6c5a4c"/>
          <stop offset="1" stop-color="#2c4f7e"/>
        </linearGradient>
        <linearGradient id="roundPhoto" x1="0" y1="0" x2="1" y2="1">
          <stop offset="0" stop-color="#c9a78f"/>
          <stop offset=".5" stop-color="#e7ddd2"/>
          <stop offset="1" stop-color="#34578a"/>
        </linearGradient>
        <linearGradient id="roomPhoto" x1="0" y1="0" x2="1" y2="1">
          <stop offset="0" stop-color="#efe9e2"/>
          <stop offset=".5" stop-color="#c9b8a5"/>
          <stop offset="1" stop-color="#45597a"/>
        </linearGradient>
      </defs>
      <rect x="0" y="0" width="681" height="525" fill="#fff"/>
      <rect x="227" y="0" width="227" height="525" fill="var(--blue)"/>
      <rect x="227" y="0" width="227" height="525" fill="var(--blue-deep)" opacity=".25"/>

      <path d="M22,0 H210 L204,28 Q202,37 192,37 H42 Q32,37 29,28 Z" fill="var(--gold)"/>
      <rect x="210" y="0" width="17" height="3" fill="var(--gold)"/>

      <path role="img" aria-label="Photo of a young boy looking down beside colorful puzzle pieces" d="M330,0 H681 V268 C620,262 530,272 475,253 C405,228 350,190 330,160 Z" fill="url(#coverPhoto)"/>
      <path d="M330,160 C350,190 405,228 475,253 C530,272 620,262 681,268" fill="none" stroke="var(--gold)" stroke-width="9"/>
      <path d="M320,172 C345,205 400,240 470,266 C525,284 620,276 681,281" fill="none" stroke="var(--blue)" stroke-width="6"/>
      <path d="M454,276 C520,292 620,284 681,288 V525 H454 Z" fill="#fff"/>

      <circle cx="567" cy="312" r="48" fill="#fff"/>
      <circle cx="567" cy="311" r="11" fill="var(--blue)"/>

      <circle cx="335" cy="93" r="66" fill="none" stroke="var(--gold)" stroke-width="5"/>
      <circle role="img" aria-label="Photo of a child playing with building blocks in a classroom" cx="335" cy="93" r="60" fill="url(#roundPhoto)" stroke="#fff" stroke-width="4"/>

      <path role="img" aria-label="Photo of a therapist playing with a toddler and stacking toys on the floor" d="M0,362 C70,340 165,345 212,398 C236,428 244,478 246,525 H0 Z" fill="url(#roomPhoto)"/>
      <path d="M0,362 C70,340 165,345 212,398 C236,428 244,478 246,525" fill="none" stroke="var(--blue)" stroke-width="7"/>
      <path d="M0,352 C75,329 172,334 222,390 C248,422 256,476 258,525" fill="none" stroke="var(--gold)" stroke-width="4"/>

      <path d="M454,525 V500 C530,488 610,484 681,476 V525 Z" fill="var(--gold)"/>
    </svg>

    <div class="tab-title about-title">ABOUT ABA THERAPY</div>
    <p class="abs about-text">ABA Therapy Applied Behavioral Analysis (ABA) Therapy is endorsed by the National Child Health Council and the Pediatric Care Association and has been scientifically proven to be the most effective in helping a child with autism to acquire the necessary skills to reach their full potential. Research has proven that</p>

    <div class="value vision">
      <h3><svg viewBox="0 0 24 24" fill="none" stroke="#b08a48" stroke-width="1.6"><path d="M2 12s4-7 10-7 10 7 10 7-4 7-10 7S2 12 2 12z"/><circle cx="12" cy="12" r="3"/><path d="M2 4V2h2M20 2h2v2M22 20v2h-2M4 22H2v-2"/></svg>Vision</h3>
      <p>To envision and strive towards a future where every child diagnosed with autism is supported, empowered, and equipped to achieve their fullest potential, fostering inclusivity and acceptance.</p>
    </div>
    <div class="value mission">
      <h3><svg viewBox="0 0 24 24" fill="none" stroke="#b08a48" stroke-width="1.6"><circle cx="11" cy="13" r="8"/><circle cx="11" cy="13" r="4"/><path d="M11 13l9-9M17 4h3v3"/></svg>Mission</h3>
      <p>We're dedicated to providing personalized, evidence-based therapy for every child with autism. Through early intervention and compassionate care, we empower growth and confidence, fostering thriving futures.</p>
    </div>
    <div class="value motto">
      <h3><svg viewBox="0 0 24 24" fill="none" stroke="#b08a48" stroke-width="1.6"><path d="M2 21l8-13 4 6 2-3 6 10z"/><path d="M10 8V3l4 1.5L10 6"/></svg>Motto</h3>
      <p>Unlocking Potential, Building Bridges, Illuminating Futures: Together, We Build Brighter Tomorrows.</p>
    </div>

    <div class="brand" style="left:227px;top:264px;width:227px;color:#fff;font-size:9.5px">
      <span class="dot" style="width:14px;height:14px;background:#fff"></span>MEADOWLARK CARE<span class="line2">BEHAVIORAL THERAPY</span>
    </div>
    <div class="contact contact-title">CONTACT US</div>
    <div class="contact contact-icons">
      <span><svg viewBox="0 0 24 24" fill="#c9a262"><path d="M12 2a7 7 0 0 0-7 7c0 5 7 13 7 13s7-8 7-13a7 7 0 0 0-7-7zm0 9.5A2.5 2.5 0 1 1 12 6.5a2.5 2.5 0 0 1 0 5z"/></svg></span>
      <span><svg viewBox="0 0 24 24" fill="#c9a262"><path d="M6.6 10.8a15 15 0 0 0 6.6 6.6l2.2-2.2c.3-.3.7-.4 1-.2 1.1.4 2.3.6 3.6.6.6 0 1 .4 1 1V20c0 .6-.4 1-1 1A17 17 0 0 1 3 4c0-.6.4-1 1-1h3.5c.6 0 1 .4 1 1 0 1.3.2 2.5.6 3.6.1.3 0 .7-.2 1z"/></svg></span>
      <span><svg viewBox="0 0 24 24" fill="none" stroke="#c9a262" stroke-width="2"><rect x="3" y="5" width="18" height="14" rx="1"/><path d="M3 6l9 7 9-7"/></svg></span>
    </div>
    <div class="contact contact-address">2718 Tamarind Ave W Suite 5<br>Minneapolis, MN 55192</div>
    <div class="contact contact-phone">612-555-0148</div>
    <div class="contact contact-email">info@meadowlarkcareaba.com</div>
    <div class="web-pill">www.meadowlarkcareaba.com</div>

    <div class="brand" style="left:454px;top:344px;width:227px;color:var(--blue);font-size:16px">MEADOWLARK CARE<span class="line2">BEHAVIORAL THERAPY</span></div>
    <div class="cover headline cover-head-1">Building Bridges to</div>
    <div class="cover headline cover-head-2">Brighter Futures</div>
    <div class="cover cover-tag">Expert Autism Therapy Services</div>
    <div class="phone-pill cover-phone"><svg viewBox="0 0 24 24" fill="#fff"><path d="M6.6 10.8a15 15 0 0 0 6.6 6.6l2.2-2.2c.3-.3.7-.4 1-.2 1.1.4 2.3.6 3.6.6.6 0 1 .4 1 1V20c0 .6-.4 1-1 1A17 17 0 0 1 3 4c0-.6.4-1 1-1h3.5c.6 0 1 .4 1 1 0 1.3.2 2.5.6 3.6.1.3 0 .7-.2 1z"/></svg>612-555-0148</div>
    <div class="cover cover-web">www.meadowlarkcareaba.com</div>
  </div>
</div>

<!-- INSIDE SPREAD -->
<div class="spread-frame inside">
  <div class="spread">
    <svg class="shapes" viewBox="0 0 681 525">
      <defs>
        <linearGradient id="livingPhoto" x1="0" y1="0" x2="1" y2="0">
          <stop offset="0" stop-color="#8a7565"/>
          <stop offset=".3" stop-color="#d2553a"/>
          <stop offset=".5" stop-color="#c23a32"/>
          <stop offset="1" stop-color="#ece6df"/>
        </linearGradient>
        <linearGradient id="ctaPhoto" x1="0" y1="0" x2="0" y2="1">
          <stop offset="0" stop-color="#1d5b97"/>
          <stop offset=".35" stop-color="#6f8db0"/>
          <stop offset="1" stop-color="#c9d4e3"/>
        </linearGradient>
        <linearGradient id="worryPhoto" x1="0" y1="0" x2="1" y2="1">
          <stop offset="0" stop-color="#e9e6e3"/>
          <stop offset="1" stop-color="#9e8b7d"/>
        </linearGradient>
      </defs>
      <rect x="0" y="0" width="681" height="525" fill="#fff"/>
      <rect x="0" y="0" width="454" height="3" fill="var(--gold)"/>
      <path d="M6,0 H222 L216,28 Q214,38 203,38 H30 Q19,38 15,28 Z" fill="var(--gold)"/>
      <rect x="454" y="0" width="227" height="525" fill="var(--blue)"/>

      <path role="img" aria-label="Photo of a mother and young son playing with toy blocks in a living room" d="M0,398 C110,378 230,382 300,412 C350,434 410,446 454,450 V525 H0 Z" fill="url(#livingPhoto)"/>
      <path d="M0,398 C110,378 230,382 300,412 C350,434 410,446 454,450" fill="none" stroke="var(--gold)" stroke-width="5"/>
      <path d="M0,388 C110,368 232,372 305,402 C355,424 412,436 454,440" fill="none" stroke="var(--blue)" stroke-width="6"/>
      <circle cx="339" cy="438" r="60" fill="none" stroke="var(--blue)" stroke-width="5"/>
      <circle role="img" aria-label="Photo of a worried parent resting her head on her hand" cx="339" cy="438" r="54" fill="url(#worryPhoto)" stroke="#fff" stroke-width="4"/>
      <path d="M382,397 A60,60 0 0 1 394,485" fill="none" stroke="var(--gold)" stroke-width="5"/>

      <rect role="img" aria-label="Photo of a therapist helping a boy stack a colorful ring toy" x="454" y="298" width="227" height="227" fill="url(#ctaPhoto)"/>
    </svg>

    <div class="tab-title services-title">OUR SERVICES</div>

    <div class="card c1 r1 gold">
      <div class="photo" role="img" aria-label="Photo of a boy in an applied behavior analysis session with a therapist" style="background:linear-gradient(135deg,#2a5d95,#9fb6cf)"></div>
      <div class="label">Applied Behavior Analysis<br>(ABA) Therapy</div>
    </div>
    <div class="card c2 r1 blue">
      <div class="photo" role="img" aria-label="Photo of a child playing with colorful building blocks" style="background:linear-gradient(135deg,#e7e2dc,#d9b35a)"></div>
      <div class="label">Occupational Therapy (OT)</div>
    </div>
    <div class="card c1 r2 blue">
      <div class="photo" role="img" aria-label="Photo of a speech therapist working with a child at a table" style="background:linear-gradient(135deg,#f1efec,#b9c2cc)"></div>
      <div class="label">Speech and Language Therapy</div>
    </div>
    <div class="card c2 r2 gold">
      <div class="photo" role="img" aria-label="Photo of children playing together at a table" style="background:linear-gradient(135deg,#d8d3cc,#7f8d7a)"></div>
      <div class="label">Social Skills Training</div>
    </div>

    <div class="brand" style="left:454px;top:58px;width:227px;color:#fff;font-size:10.5px">
      <span class="dot" style="width:16px;height:16px;background:#fff"></span>MEADOWLARK CARE<span class="line2">BEHAVIORAL THERAPY</span>
    </div>
    <div class="cta cta-head-1">READY TO TAKE THE</div>
    <div class="cta cta-head-2">NEXT STEP?</div>
    <div class="cta cta-star">★</div>
    <div class="cta cta-tag">Contact Us Today for Expert<br>Autism Therapy Services!</div>
    <div class="phone-pill cta-phone"><svg viewBox="0 0 24 24" fill="#fff"><path d="M6.6 10.8a15 15 0 0 0 6.6 6.6l2.2-2.2c.3-.3.7-.4 1-.2 1.1.4 2.3.6 3.6.6.6 0 1 .4 1 1V20c0 .6-.4 1-1 1A17 17 0 0 1 3 4c0-.6.4-1 1-1h3.5c.6 0 1 .4 1 1 0 1.3.2 2.5.6 3.6.1.3 0 .7-.2 1z"/></svg>612-555-0148</div>
    <div class="cta cta-web">www.meadowlarkcareaba.com</div>
  </div>
</div>

</body>
</html>
```